Stationery Design Project

Would like to have the design elements we created in for our website (www.brook-estates.com), incorporated in a stationery design layout.
Updates
Colors used in the logo attachments do not need to be used. We are open to different color variations. Looking for a crisp, clean, modern update using the design elements in attachments and which can also be viewed on or website.
A note to designers:
Project Deadline Extended
Reason: Due to update in our project description and requirements, we have decided to extend the deadline of this project to provide ample opportunity to all designers participating .
Requirements
Must have
- Must have continuity with the theme and design features used in our website. Have attached .jpg images of some of the design elements.

```html
<!DOCTYPE html>
<html lang="en">
<head>
<meta charset="utf-8">
<title>Brook Estates Letterhead</title>
<link rel="stylesheet" href="https://fonts.googleapis.com/css2?family=Open+Sans:wght@400;600;700&display=swap">
<style>
  :root {
    --backdrop: #e9e6e1;
    --paper: #ffffff;
    --leaf-green: #e3f2d0;
    --stream-blue: #cfe2f2;
    --brand-blue: #3f8fcf;
    --brand-green: #8cc63f;
    --ink: #1a1a1a;
  }
  * { margin: 0; padding: 0; box-sizing: border-box; }
  html, body {
    width: 1200px;
    height: 900px;
    overflow: hidden;
    background: var(--backdrop);
    font-family: "Open Sans", Arial, sans-serif;
  }
  .canvas {
    position: relative;
    width: 1200px;
    height: 900px;
  }
  .letterhead {
    position: absolute;
    left: 334px;
    top: 74px;
    width: 532px;
    height: 750px;
    background: var(--paper);
    box-shadow: 0 2px 10px rgba(0, 0, 0, 0.18);
    overflow: hidden;
  }
  .side-illustration {
    position: absolute;
    left: 0;
    top: 0;
    width: 214px;
    height: 750px;
    background: linear-gradient(to right, var(--leaf-green) 0%, var(--leaf-green) 70%, var(--stream-blue) 100%);
  }
  .masthead-name {
    position: absolute;
    right: 24px;
    top: 40px;
    font-size: 22px;
    font-weight: 400;
    color: var(--ink);
  }
  .contact-block {
    position: absolute;
    left: 346px;
    top: 656px;
  }
  .company-name {
    display: flex;
    align-items: center;
    gap: 5px;
    font-size: 19px;
    font-weight: 400;
    color: var(--brand-blue);
    line-height: 1.1;
    margin-bottom: 3px;
  }
  .company-dot {
    width: 9px;
    height: 9px;
    border-radius: 50%;
    background: var(--brand-green);
    flex: none;
  }
  .contact-line {
    font-size: 10.5px;
    font-weight: 600;
    color: var(--ink);
    line-height: 1.33;
  }
</style>
</head>
<body>
<div class="canvas">
  <div class="letterhead">
    <div class="side-illustration" role="img" aria-label="Large pale green leaf with a soft blue swoosh curving down the left edge"></div>

    <div class="masthead-name">Brook Estates</div>

    <div class="contact-block">
      <div class="company-name"><span class="company-dot"></span>Brook Estates, Inc.</div>
      <p class="contact-line">418 Willow Creek Road Suite 120</p>
      <p class="contact-line">Maple Falls, GA 30812</p>
      <p class="contact-line">PHONE: (555) 214-6630</p>
      <p class="contact-line">FAX : (555) 214-6631</p>
      <p class="contact-line">E-mail us: info@brook-estates.com</p>
    </div>
  </div>
</div>
</body>
</html>
```